Catering Menu Package

I currently have a complete menu package, which we have redesigned as far as content, now I need to it put together in a catalog type format. It is essentially 10-12 pages in length, and will be sent for print production. Upon receiving a final edit
Updates

I have added an example gif to the project.

I did this free hand this basically what I am looking for. please change text and type to whatever you think would look best. This is a total rough design so, feel free to change any and everything. The text for the page is on the word documents. If you need more images let me know I am in the process of getting as many images uploaded for your use.

Reason: I figured we got a late jump with questions, so i am extending a few days .

Target Market(s)

The target market is business who wish to have catered luncheons, breakfasts , meetings

Industry/Entity Type

Catering

Requirements
Must have
• I have attached a copy of the text that what we want in the package, our logo, and i have also attached a catering package of another company to give you an idea what the finished product will be
Should not have
• It should not look identical to the example catering packages, these are for some inspiration we want our own design with the same type of look and feel

```html
<!DOCTYPE html>
<html lang="en">
<head>
<meta charset="utf-8">
<title>Ala Carte Sides and Signature Soups</title>
<link href="https://fonts.googleapis.com/css2?family=Parisienne&family=Kalam:wght@300;400&display=swap" rel="stylesheet">
<style>
  :root {
    --paper: #ebe5d8;
    --paper-deep: #e0d9ca;
    --ink: #2a2522;
    --rule: #1e1b19;
    --brand-mark: #e07a2c;
  }
  html, body {
    margin: 0;
    padding: 0;
    width: 1200px;
    height: 928px;
    overflow: hidden;
  }
  .menu-page {
    position: relative;
    width: 1200px;
    height: 928px;
    color: var(--ink);
    font-family: "Kalam", cursive;
    font-weight: 300;
    overflow: hidden;
  }
  .page-texture {
    position: absolute;
    inset: 0;
    background: radial-gradient(ellipse at 50% 50%, var(--paper) 0%, var(--paper-deep) 100%);
  }
  .section-title {
    position: absolute;
    margin: 0;
    font-family: "Parisienne", cursive;
    font-weight: 400;
    font-size: 44px;
    line-height: 1;
  }
  .sides-title { left: 70px; top: 82px; }
  .soups-title { right: 30px; top: 64px; }

  .sides-list {
    position: absolute;
    left: 73px;
    top: 132px;
    margin: 0;
    padding: 0;
    list-style: none;
    font-size: 18px;
    line-height: 31.8px;
  }

  .column-rule {
    position: absolute;
    left: 425px;
    top: 47px;
    width: 3px;
    height: 795px;
    background: var(--rule);
  }

  .brand {
    position: absolute;
    left: 72px;
    top: 700px;
    width: 96px;
    text-align: center;
    font-size: 17px;
    line-height: 21px;
  }
  .brand-square {
    display: block;
    width: 40px;
    height: 40px;
    margin: 0 auto 10px;
    background: var(--brand-mark);
  }

  .soups-note {
    position: absolute;
    right: 30px;
    top: 104px;
    margin: 0;
    font-size: 17px;
  }
  .soup {
    position: absolute;
    right: 30px;
    margin: 0;
    text-align: right;
    font-size: 17px;
    line-height: 21.5px;
    white-space: nowrap;
  }
  .soup-name, .soup-desc { display: block; }
</style>
</head>
<body>
<main class="menu-page">
  <div class="page-texture" role="img" aria-label="Soft beige paper background with a faint swirling floral pattern"></div>

  <h2 class="section-title sides-title">Ala Carte Sides</h2>
  <ul class="sides-list">
    <li>Lemon Scented Petit Green Beans</li>
    <li>Tomato-Zucchini Casserole</li>
    <li>Steamed Broccoli</li>
    <li>Maple Glazed Carrots</li>
    <li>Sautéed Local Corn</li>
    <li>Pasta Vegetable Salad</li>
    <li>Country Potato Salad</li>
    <li>Asparagus and Petit Green Bean Salad</li>
    <li>Oven Roasted Redskin Potatoes</li>
    <li>Balsamic Roasted Seasonal Vegetable Medley</li>
    <li>Creamy Cole Slaw</li>
    <li>Caprese Salad</li>
    <li>Jeweled Rice</li>
    <li>Pineapple Hawaiian Cole Slaw</li>
    <li>Fresh Watermelon Wedges</li>
    <li>Fresh Fruit and Melon Platter</li>
  </ul>

  <div class="brand">
    <span class="brand-square"></span>
    harbor<br>table<br>caterers
  </div>

  <div class="column-rule"></div>

  <h2 class="section-title soups-title">Signature Soups</h2>
  <p class="soups-note">all Served with fresh Baked Sourdough Baguettes</p>

  <p class="soup" style="top:148px">
    <span class="soup-name">Cream of Crab Soup-</span>
    <span class="soup-desc">Rich and and Creamy Maryland Classic finished with Sherry Wine</span>
    <span class="soup-desc">.</span>
  </p>
  <p class="soup" style="top:211px">
    <span class="soup-name">Maryland Hard Crab Soup-</span>
    <span class="soup-desc">Maryland’s traditional Crab Soup, loaded with fresh Vegetables and Lump Crab Meat.</span>
  </p>
  <p class="soup" style="top:274px">
    <span class="soup-name">Seafood Bisque-</span>
    <span class="soup-desc">Scallops, Crab, Salmon, and Lobster in a Rich and Creamy Broth, Spiked with Brandy.</span>
  </p>
  <p class="soup" style="top:337px">
    <span class="soup-name">Chef Mateo’ Creamy Tortilla Soup-</span>
    <span class="soup-desc">An HTC favorite.&nbsp; Delicious with just a hint of spice, served with Crispy Tortilla Strips,</span>
    <span class="soup-desc">Great Vegetarian Soup! Want Chicken, no problem.</span>
  </p>
  <p class="soup" style="top:421px">
    <span class="soup-name">Grilled Seasonal Vegetable Gazpacho-</span>
    <span class="soup-desc">Perfect for hot summer days!&nbsp; Served chilled with a Cilantro Pesto.</span>
  </p>
  <p class="soup" style="top:486px">
    <span class="soup-name">Country Chicken Noodle-</span>
    <span class="soup-desc">Grandma’s Recipe, Flavorful broth and plenty of chicken. Pair with one of our Sandwiches</span>
    <span class="soup-desc">.</span>
  </p>
  <p class="soup" style="top:551px">
    <span class="soup-name">Fire-Roasted Tomato Bisque-</span>
    <span class="soup-desc">Creamy tomato soup.&nbsp; Finished with Parmsan-Garlic Croutons.Vegetarian.</span>
  </p>
  <p class="soup" style="top:613px">
    <span class="soup-name">Navy Bean and Country Ham-</span>
    <span class="soup-desc">Made with just like Grandma used to with the Smoked Ham hocks.</span>
  </p>
  <p class="soup" style="top:677px">
    <span class="soup-name">Creamy Brocoli &amp; Cheddar Soup</span>
  </p>
  <p class="soup" style="top:720px">
    <span class="soup-name">Beef Vegetable-</span>
    <span class="soup-desc">Chef Dalton’s secret recipe!&nbsp; Slow cooked with generous amounts of Beef and seasonal Vegetables.</span>
  </p>
</main>
</body>
</html>
```